Dentistry

Dentist's personal business card. No logo needed. The card shoul deliver the massage of reliability, professionalism, experience.
Please ad the full brief of the project: down the line it says: the winning look should be precise and pristine NO pictures of Teeth, smiles, instruments etc.

The details to be desplaid are:
Dr. Rob Valdoni
Doctor of Dental Surgery
PHD
Web. Www.drvaldoni.com
Email. Rob@drvaldoni.com
Tel 07731482590
Surgery address. 27Bharwick road London SW4 7QN UK
82 Fenwyn Row London SW3 2HT. Uk

Reason: Decided to make the payment unrefundable in order to get more designers involved.

Requirements
Should not have
• Logo, teeth, smile any sort of instruments.

```html
<!DOCTYPE html>
<html lang="en">
<head>
<meta charset="utf-8">
<title>Dr. Elian Morrow — Business Card</title>
<link href="https://fonts.googleapis.com/css2?family=Cinzel:wght@400&family=Cormorant+Garamond:wght@400;500&display=swap" rel="stylesheet">
<style>
  :root {
    --backdrop: #2c2c2c;
    --front-top-light: #c6c2be;
    --front-top-dark: #a8a4a0;
    --front-bottom-light: #e6e1da;
    --front-bottom-dark: #d8d3cc;
    --accent-teal: #1ea9ba;
    --back-light: #d5d8db;
    --back-mid: #c2c5c8;
    --back-dark: #aaaeb2;
    --pattern-light: #b9b6b3;
    --pattern-dark: #9fa2a6;
    --ink: #6f6c69;
    --ink-soft: #8a8784;
  }
  html, body {
    margin: 0;
    width: 1200px;
    height: 900px;
    overflow: hidden;
    background: var(--backdrop);
  }
  .canvas {
    position: relative;
    width: 1200px;
    height: 900px;
  }
  .card {
    position: absolute;
    top: 313px;
    width: 480px;
    height: 274px;
    overflow: hidden;
    box-shadow: 0 10px 30px rgba(0,0,0,0.45);
  }
  .card--front { left: 90px; }
  .card--back {
    left: 630px;
    background: linear-gradient(135deg, var(--back-light) 0%, var(--back-mid) 55%, var(--back-dark) 100%);
  }

  /* Front */
  .front-top {
    position: absolute;
    left: 0; right: 0; top: 0;
    height: 138px;
    background: linear-gradient(120deg, var(--front-top-light), var(--front-top-dark));
  }
  .front-pattern {
    position: absolute;
    left: 0; right: 0; top: 0;
    height: 138px;
    background: radial-gradient(ellipse at 70% 45%, var(--pattern-light) 0%, rgba(185,182,179,0) 70%);
  }
  .front-rule {
    position: absolute;
    left: 0; right: 0;
    top: 138px;
    height: 4px;
    background: var(--accent-teal);
  }
  .front-bottom {
    position: absolute;
    left: 0; right: 0;
    top: 142px; bottom: 0;
    background: linear-gradient(160deg, var(--front-bottom-light), var(--front-bottom-dark));
  }
  .front-identity {
    position: absolute;
    left: 0; right: 0;
    top: 190px;
    text-align: center;
    color: var(--ink);
  }
  .doctor-name {
    font-family: "Cinzel", serif;
    font-weight: 400;
    margin: 0;
    letter-spacing: 0.5px;
  }
  .front-identity .doctor-name { font-size: 15px; }
  .doctor-role {
    font-family: "Cormorant Garamond", serif;
    font-size: 8px;
    letter-spacing: 4px;
    text-transform: uppercase;
    margin: 4px 0 0;
    color: var(--ink-soft);
  }

  /* Back */
  .back-pattern {
    position: absolute;
    left: 0; right: 0; bottom: 0;
    height: 160px;
    background: linear-gradient(180deg, rgba(159,162,166,0) 0%, var(--pattern-dark) 100%);
    opacity: 0.6;
  }
  .back-details {
    position: absolute;
    left: 40px;
    top: 32px;
    color: var(--ink);
  }
  .back-details .doctor-name { font-size: 16px; margin-bottom: 14px; }
  .contact-line {
    font-family: "Cormorant Garamond", serif;
    font-size: 12px;
    line-height: 16px;
    margin: 0;
    color: var(--ink-soft);
  }
</style>
</head>
<body>
<main class="canvas">

  <section class="card card--front" aria-label="Card front">
    <div class="front-top"></div>
    <div class="front-pattern" role="img" aria-label="Soft area for the light geometric background motif"></div>
    <div class="front-rule"></div>
    <div class="front-bottom"></div>
    <div class="front-identity">
      <h1 class="doctor-name">Dr. Elian Morrow</h1>
      <p class="doctor-role">Dental Office</p>
    </div>
  </section>

  <section class="card card--back" aria-label="Card back">
    <div class="back-pattern" role="img" aria-label="Soft area for the grey geometric background motif"></div>
    <div class="back-details">
      <h2 class="doctor-name">Dr. Elian Morrow, DMD</h2>
      <p class="contact-line">12 Larkfield Lane, Townsby</p>
      <p class="contact-line">elian@morrowdental.example</p>
      <p class="contact-line">555-014-2290</p>
    </div>
  </section>

</main>
</body>
</html>
```